Landing Page für Freelancer im Bereich der Informationstechnik
Zielgruppe
Ich bin Experte für Informationstechnik, Unified Communications, Beratung, Management sowie Projekte aller Art.
Mit meiner WOLKENTOR GmbH bin ich als (einzelner) Freelancer für mittelständische Unternehmen und Konzerne in verschiedensten Projekten tätig.
Mein Motto lautet 'Mit Präzision und langjähriger Erfahrung immer alles im Griff!'
Aufgabenstellung
Die aktuell existierende Internet-Präsenz unter wolkentor-web.de beinhaltet aktuell nur eine minimalistische statische Seite sowie das Impressum, ohne jegliche dynamische Inhalte.
DABEI SOLL ES BLEIBEN. Auch die Inhalte sollen unverändert übernommen werden.
Lediglich soll jetzt eine Anlehnung an das zwischenzeitlich vorhandene Logo vorgenommen werden, welches ich mitliefere.
Es geht mir insgesamt nur darum, ein professionelleres Auftreten zu haben, WENN sich denn mal jemand auf die Seite verirrt.
Das Aussehen soll daher modern und dynamisch sein.
ZUSAMMENFASSUNG: Inhalte bleiben 1:1, grafische Anpassung an Logo gewünscht.
Technisch: Statisch, kein Content-Management. Lohnt sich hier nicht.
SEHR WICHTIG: Ich möchte gerne, dass die Lieferung bereits als HTML (und NICHT NUR ALS GRAFIK) erfolgt, ggf. stelle ich auch kurz den FTP-Zugang.
Insgesamt möchte ich gar keine große Sache draus machen.
Viele Anpassungsrunden wird es voraussichtlich nicht geben.
Zeitlich ist dies hier ein sehr kleines Projekt - Erweiterungen kommen später.

```html
<!DOCTYPE html>
<html lang="de">
<head>
<meta charset="utf-8">
<title>Lukas Martin Brenner – WOLKENTOR GmbH</title>
<link rel="stylesheet" href="https://fonts.googleapis.com/css2?family=Exo+2:ital,wght@0,800;1,500&family=Open+Sans:wght@400;600;700&display=swap">
<style>
  :root {
    --teal: #3d9fbc;
    --tile: #d7d8d9;
    --tile-tab: #cfd0d1;
    --ink: #3a3a3a;
    --muted: #555;
    --page: #ffffff;
  }
  * { margin: 0; padding: 0; box-sizing: border-box; }
  html, body { width: 1200px; height: 800px; overflow: hidden; background: var(--page); }
  body { font-family: "Open Sans", Arial, sans-serif; color: var(--ink); }
  .page { position: relative; width: 1200px; height: 800px; overflow: hidden; }

  .brand {
    position: absolute; top: 56px; right: 70px;
    display: flex; align-items: center; gap: 10px;
    font-family: "Open Sans", Arial, sans-serif; font-weight: 600;
    font-size: 20px; letter-spacing: 2px; color: var(--teal);
  }
  .brand-dot { width: 14px; height: 14px; border-radius: 50%; background: var(--teal); }

  .hero-name {
    position: absolute; left: 70px; top: 118px;
    font-family: "Exo 2", Arial, sans-serif; font-weight: 800;
    font-size: 70px; line-height: 1; color: var(--teal); letter-spacing: 1px;
    text-transform: uppercase;
  }
  .hero-degrees {
    position: absolute; left: 74px; top: 212px;
    font-size: 21px; line-height: 1.35; color: var(--muted);
  }

  .tile {
    position: absolute; background: var(--tile);
    border-radius: 4px 0 4px 4px;
    display: flex; flex-direction: column; align-items: center; justify-content: center; gap: 18px;
  }
  .tile::before {
    content: ""; position: absolute; top: -16px; right: 0;
    width: 62%; height: 18px; background: var(--tile);
    clip-path: polygon(12% 0, 100% 0, 100% 100%, 0 100%);
    border-radius: 3px 3px 0 0;
  }
  .tile-label { font-size: 15px; font-weight: 600; color: var(--ink); text-align: center; }
  .tile svg { display: block; }
  .tile-expert   { left: 70px;  top: 330px; width: 260px; height: 190px; }
  .tile-uc       { left: 360px; top: 330px; width: 240px; height: 190px; }
  .tile-advice   { left: 70px;  top: 565px; width: 170px; height: 170px; }
  .tile-mgmt     { left: 260px; top: 565px; width: 160px; height: 170px; }
  .tile-projects { left: 440px; top: 565px; width: 160px; height: 170px; }

  .motto {
    position: absolute; left: 690px; top: 300px; width: 440px;
    font-family: "Exo 2", Arial, sans-serif; font-style: italic; font-weight: 500;
    font-size: 26px; line-height: 1.3; color: var(--teal); text-align: center;
  }
  .contact {
    position: absolute; left: 700px; top: 470px; width: 440px;
    font-size: 14px; line-height: 1.55; color: var(--muted);
  }
  .contact p + p { margin-top: 16px; }
  .contact strong { color: var(--ink); font-weight: 700; }
  .legal-links {
    position: absolute; left: 700px; top: 640px;
    font-size: 14px; color: var(--muted);
  }
  .legal-links a { color: var(--muted); text-decoration: underline; }
</style>
</head>
<body>
<main class="page">
  <div class="brand"><span class="brand-dot"></span>WOLKENTOR GmbH</div>

  <h1 class="hero-name">Lukas Martin Brenner</h1>
  <p class="hero-degrees">Diplom-Informatiker (FH)<br>Master of Science in Electronic Business</p>

  <section class="tile tile-expert">
    <span class="tile-label">Experte für Informationstechnik</span>
    <svg width="64" height="64" viewBox="0 0 64 64" aria-hidden="true">
      <polygon points="32,2 58,17 58,47 32,62 6,47 6,17" fill="var(--teal)"/>
      <text x="32" y="40" text-anchor="middle" font-family="Exo 2, sans-serif" font-weight="800" font-size="20" fill="#fff">PRO</text>
    </svg>
  </section>

  <section class="tile tile-uc">
    <span class="tile-label">Unified Communications</span>
    <svg width="64" height="60" viewBox="0 0 64 60" aria-hidden="true">
      <path d="M32 4C16 4 4 14 4 28c0 8 4 14 10 18l-4 12 14-8c2.5.6 5 1 8 1 16 0 28-10 28-23S48 4 32 4z" fill="var(--teal)"/>
      <circle cx="20" cy="28" r="4" fill="#fff"/><circle cx="32" cy="28" r="4" fill="#fff"/><circle cx="44" cy="28" r="4" fill="#fff"/>
    </svg>
  </section>

  <section class="tile tile-advice">
    <span class="tile-label">Beratung</span>
    <svg width="48" height="48" viewBox="0 0 48 48" aria-hidden="true">
      <path d="M10 8l8 0 4 10-5 4c2 5 6 9 11 11l4-5 10 4v8c0 2-2 4-4 4C19 44 4 29 4 12c0-2 2-4 4-4z" fill="var(--teal)"/>
      <circle cx="34" cy="14" r="10" fill="var(--teal)"/>
      <path d="M34 9v10M29 14h10" stroke="#fff" stroke-width="2.5" stroke-linecap="round"/>
    </svg>
  </section>

  <section class="tile tile-mgmt">
    <span class="tile-label">Management</span>
    <svg width="44" height="52" viewBox="0 0 44 52" aria-hidden="true">
      <rect x="4" y="8" width="18" height="42" fill="var(--teal)"/>
      <rect x="22" y="2" width="18" height="48" fill="var(--teal)" opacity=".8"/>
      <g fill="#fff">
        <rect x="8" y="14" width="4" height="4"/><rect x="14" y="14" width="4" height="4"/>
        <rect x="8" y="24" width="4" height="4"/><rect x="14" y="24" width="4" height="4"/>
        <rect x="26" y="10" width="4" height="4"/><rect x="32" y="10" width="4" height="4"/>
        <rect x="26" y="20" width="4" height="4"/><rect x="32" y="20" width="4" height="4"/>
        <rect x="28" y="38" width="6" height="12"/>
      </g>
    </svg>
  </section>

  <section class="tile tile-projects">
    <span class="tile-label">Projekte aller Art</span>
    <svg width="44" height="50" viewBox="0 0 44 50" aria-hidden="true">
      <rect x="4" y="6" width="36" height="42" rx="3" fill="var(--teal)"/>
      <rect x="14" y="2" width="16" height="8" rx="2" fill="var(--teal)" stroke="#fff" stroke-width="2"/>
      <path d="M10 34l8-8 6 5 10-11" stroke="#fff" stroke-width="3" fill="none" stroke-linecap="round" stroke-linejoin="round"/>
      <path d="M10 41h24" stroke="#fff" stroke-width="3" stroke-linecap="round"/>
    </svg>
  </section>

  <p class="motto">Mit Präzision und langjähriger Erfahrung<br>immer alles im Griff!</p>

  <div class="contact">
    <p>Gerne schicke ich Ihnen unverbindlich mein Expertenprofil samt CV sowie meine aktuellen Verfügbarkeiten zu.</p>
    <p>Kontaktieren Sie mich hierzu einfach per E-Mail unter <strong>l punkt brenner at Wolkentor punkt de</strong>. Ich freue mich auf Sie!</p>
  </div>

  <p class="legal-links">[ <a href="#impressum">Impressum / Datenschutzerklärung</a> ]</p>
</main>
</body>
</html>
```